Book cover for middle grade children's book

I need a book cover design for the first book in my middle grade series aimed at girls ages 9-12.

PLEASE SEE MY ATTACHED EXAMPLES.

Title: Lila Dorsey: Cousin Marla's Scheme

Design Brief:
Front: I want it to look like a composition book. The background should be a pink plaid design. There should be a white square in the center like a composition book. On top of the square in purple letters should be the name Lila. Underneath the square should be the name Dorsey. Lila Dorsey should be in a fun girly font that's readible on thumbnail. The sub title should go on the white square where a kid would write their name. It should say Cousin Marla's Scheme in a girl's pink handwriting. At the bottom underneath Dorsey should be my name: Rochelle Anne Vukovic

On the left side there should be a dark pink or purple (whichever looks best with the pattern) strip like composition books have.

Spine: Lila Dorsey: Cousin Marla's Scheme (Lila Dorsey #1) Vukovic

On the back: I'd like the back to be hot pink with white font.

Thirteen-year-old Lila Dorsey has a lot on her plate. Her biggest challenge is living with her Cousin Marla. As much as Lila tries to please her aunt,, they always seem to butt heads. Sometimes Lila feels as if Cousin Marla goes out of her way to make her life miserable.

Cousin Marla enrolls Lila in a social group called the Golden Tulips, a group that's supposed to teach young girls how to be proper ladies, however it turns out to be nothing more than a club for snobs. Lila wants out, but she's made a deal with Cousin Marla. Will Lila take a stand against the Golden Tulips or will their snobbery rub off on her?
IT'S VERY IMPORTANT THAT IT LOOKS LIKE A COMPOSITION BOOK SINCE THAT WILL BE THE BRAND FOR THE SERIES.

I need this cover to fit the mandates for ebook and printhollow. Place follow the correct measurements.

This book will be 160 pages on cream paper. 6x9

Target Market(s)

Girls ages 9 and up

Industry/Entity Type

Club

Requirements
Must have
• Readable professional looking font
Should not have
• A background pattern that too busy and clashes with the font

```html
<!DOCTYPE html>
<html lang="en">
<head>
<meta charset="utf-8">
<title>Lila Dorsey: Cousin Marla's Scheme – Cover</title>
<link rel="stylesheet" href="https://fonts.googleapis.com/css2?family=Mystery+Quest&family=Sue+Ellen+Francisco&family=Arimo&display=swap">
<style>
  :root {
    --page-bg: #ffffff;
    --plum: #8b2a57;
    --plum-dark: #7a2149;
    --front-pink-light: #fbe3ec;
    --front-pink: #f4c6d7;
    --back-pink: #ee6fa8;
    --label-white: #ffffff;
    --back-text: #ffffff;
    --shadow: rgba(0, 0, 0, 0.18);
  }
  * { margin: 0; padding: 0; box-sizing: border-box; }
  html, body {
    width: 1200px;
    height: 874px;
    overflow: hidden;
    background: var(--page-bg);
  }
  .canvas {
    position: relative;
    width: 1200px;
    height: 874px;
  }
  .front-cover, .back-cover {
    position: absolute;
    top: 82px;
    width: 469px;
    height: 715px;
    box-shadow: 6px 10px 18px var(--shadow);
  }
  .front-cover { left: 100px; }
  .back-cover {
    left: 625px;
    background: var(--back-pink);
  }
  .pattern-fill {
    position: absolute;
    inset: 0;
  }
  .front-cover .pattern-fill {
    background: linear-gradient(180deg, var(--front-pink-light) 0%, var(--front-pink) 55%, var(--front-pink-light) 100%);
  }
  .back-cover .pattern-fill {
    background: linear-gradient(180deg, #f078ad 0%, var(--back-pink) 100%);
  }
  .spine-strip {
    position: absolute;
    left: 0;
    top: 0;
    width: 73px;
    height: 100%;
    background: var(--plum);
  }
  .spine-text {
    position: absolute;
    left: 36px;
    top: 50%;
    width: 700px;
    transform: translate(-50%, -50%) rotate(-90deg);
    text-align: center;
    white-space: nowrap;
    font-family: "Mystery Quest", cursive;
    font-size: 16px;
    letter-spacing: 0.5px;
    color: var(--label-white);
  }
  .series-name {
    position: absolute;
    left: 73px;
    right: 0;
    text-align: center;
    font-family: "Mystery Quest", cursive;
    font-size: 80px;
    line-height: 1;
    color: var(--plum);
  }
  .series-first { top: 100px; }
  .series-last { top: 365px; }
  .name-label {
    position: absolute;
    left: 127px;
    top: 230px;
    width: 268px;
    height: 124px;
    background: var(--label-white);
    border-radius: 14px;
    padding: 9px;
  }
  .name-label-inner {
    width: 100%;
    height: 100%;
    background: var(--plum);
    border-radius: 10px;
    display: flex;
    align-items: center;
    justify-content: center;
    text-align: center;
  }
  .book-title {
    font-family: "Mystery Quest", cursive;
    font-weight: normal;
    font-size: 37px;
    line-height: 1.12;
    color: var(--label-white);
  }
  .author-name {
    position: absolute;
    left: 73px;
    right: 0;
    top: 700px;
    transform: translateY(-100%);
    text-align: center;
    font-family: "Sue Ellen Francisco", cursive;
    font-size: 46px;
    line-height: 1;
    color: var(--plum);
  }
  .blurb {
    position: absolute;
    left: 17px;
    right: 17px;
    top: 53px;
    font-family: "Arimo", Arial, sans-serif;
    font-size: 14.2px;
    line-height: 17.4px;
    color: var(--back-text);
    text-align: justify;
  }
  .blurb p { text-indent: 22px; }
  .blurb p + p { margin-top: 17px; }
</style>
</head>
<body>
<main class="canvas">
  <section class="front-cover" aria-label="Front cover">
    <div class="pattern-fill" role="img" aria-label="Soft pink diamond plaid pattern background"></div>
    <div class="spine-strip">
      <p class="spine-text">Lila Dorsey: Cousin Marla's Scheme (Lila Dorsey #1) Vukovic</p>
    </div>
    <p class="series-name series-first">Lila</p>
    <div class="name-label">
      <div class="name-label-inner">
        <h1 class="book-title">Cousin Marla's<br>Scheme</h1>
      </div>
    </div>
    <p class="series-name series-last">Dorsey</p>
    <p class="author-name">Rochelle Anne Vukovic</p>
  </section>

  <section class="back-cover" aria-label="Back cover">
    <div class="pattern-fill" role="img" aria-label="Hot pink crosshatch plaid pattern background"></div>
    <div class="blurb">
      <p>Thirteen-year-old Lila Dorsey has a lot on her plate. Her biggest challenge is living with her Cousin Marla. As much as Lila tries to please her aunt,, they always seem to butt heads. Sometimes Lila feels as if Cousin Marla goes out of her way to make her life miserable.</p>
      <p>Cousin Marla enrolls Lila in a social group called the Golden Tulips, a group that's supposed to teach young girls how to be proper ladies, however it turns out to be nothing more than a club for snobs. Lila wants out, but she's made a deal with Cousin Marla. Will Lila take a stand against the Golden Tulips or will their snobbery rub off on her?</p>
    </div>
  </section>
</main>
</body>
</html>
```